Coaching and Tutoring that removes all obstacles and leads to success and happiness

Tutoring maths giving confidence, clarity and success to students of all abilities. Tutoring from 14 years to 18 years old. Dealing with exam preparation and stress.
Coaching confidence, resilience and ultimately happiness and freedom.
The design to inspire and reassure people of a safe pair of hands as well excitement of the beginning of something new in their lives.

Target Market(s)

20 -30 year olds

Industry/Entity Type

Self Development and Education

Contact Information for Business Card

Confidence Coach and Maths Tutor

Font styles to use
Sans Serif

Colors
EE7325
F08F49
F5BC92
FAE3D3
FDF4ED

Requirements
Must have
• Success and Happiness

```html
<!DOCTYPE html>
<html lang="en">
<head>
<meta charset="utf-8">
<title>Maple Brook Coaching – Business Card</title>
<link href="https://fonts.googleapis.com/css2?family=Cinzel:wght@400&family=Arimo:wght@400;700&display=swap" rel="stylesheet">
<style>
  :root {
    --stage: #1c1c1c;
    --stage-edge: #0e0e0e;
    --card-white: #ffffff;
    --brand-green: #82b23a;
    --brand-orange: #ee7325;
    --ink: #2b2b2b;
    --photo-sky: #d9d6c8;
    --photo-sun: #f4efdc;
    --photo-hill: #2f3320;
    --photo-shadow: #151811;
  }
  * { margin: 0; padding: 0; box-sizing: border-box; }
  html, body { width: 1200px; height: 1015px; overflow: hidden; }
  body {
    background: radial-gradient(ellipse at 45% 35%, var(--stage) 0%, var(--stage-edge) 100%);
    position: relative;
    font-family: "Arimo", Arial, sans-serif;
  }
  .card {
    position: absolute;
    width: 620px;
    height: 354px;
    box-shadow: 0 18px 40px rgba(0,0,0,0.6);
    overflow: hidden;
  }
  /* Front side */
  .card--front { left: 110px; top: 100px; }
  .front-photo {
    position: absolute; inset: 0;
    background:
      radial-gradient(circle at 42% 38%, var(--photo-sun) 0%, rgba(244,239,220,0.6) 14%, rgba(217,214,200,0) 38%),
      linear-gradient(180deg, var(--photo-sky) 0%, #9c9a88 38%, var(--photo-hill) 62%, var(--photo-shadow) 100%);
  }
  .front-tagline {
    position: absolute;
    left: 0; right: 0; bottom: 58px;
    text-align: center;
    color: var(--card-white);
    font-family: "Arimo", Arial, sans-serif;
    font-weight: 700;
    font-size: 30px;
    letter-spacing: 1px;
    text-shadow: 0 2px 6px rgba(0,0,0,0.5);
  }
  /* Back side */
  .card--back { left: 470px; top: 560px; background: var(--card-white); }
  .brand {
    position: absolute; left: 40px; top: 70px;
    display: flex; align-items: center; gap: 22px;
  }
  .brand-dot {
    width: 78px; height: 78px; border-radius: 50%;
    background: var(--brand-orange);
  }
  .brand-name {
    font-family: "Cinzel", Georgia, serif;
    font-weight: 400;
    color: var(--brand-green);
    font-size: 36px;
    line-height: 1.05;
    letter-spacing: 1px;
  }
  .brand-name .brand-sub { display: block; font-size: 20px; letter-spacing: 9px; }
  .person {
    position: absolute; left: 190px; top: 170px;
    color: var(--ink);
  }
  .person-name {
    font-family: "Cinzel", Georgia, serif;
    color: var(--brand-green);
    font-size: 26px;
    letter-spacing: 1px;
    line-height: 1;
  }
  .person-role { font-size: 15px; margin-top: 2px; }
  .contacts { list-style: none; margin-top: 10px; font-size: 15px; line-height: 21px; }
  .contacts li { display: flex; align-items: center; gap: 8px; }
  .contacts svg { width: 14px; height: 14px; flex: none; }
  .contacts .accent { color: var(--brand-green); }
  .address { margin-top: 10px; font-size: 15px; line-height: 19px; }
</style>
</head>
<body>

  <section class="card card--front">
    <div class="front-photo" role="img" aria-label="Photograph of a person walking through a wooden gate on a hillside path toward a bright low sun"></div>
    <p class="front-tagline">SUCCESS AND HAPPINESS</p>
  </section>

  <section class="card card--back">
    <div class="brand">
      <span class="brand-dot"></span>
      <p class="brand-name">MAPLE BROOK<span class="brand-sub">COACHING</span></p>
    </div>

    <div class="person">
      <h1 class="person-name">DANIEL REED</h1>
      <p class="person-role">Managing Director</p>
      <ul class="contacts">
        <li>
          <svg viewBox="0 0 24 24" aria-hidden="true"><path fill="#ee7325" d="M6.6 10.8a15 15 0 0 0 6.6 6.6l2.2-2.2a1 1 0 0 1 1-.25 11.4 11.4 0 0 0 3.6.57 1 1 0 0 1 1 1V20a1 1 0 0 1-1 1A17 17 0 0 1 3 4a1 1 0 0 1 1-1h3.5a1 1 0 0 1 1 1c0 1.25.2 2.45.57 3.57a1 1 0 0 1-.25 1z"/></svg>
          020-555 014 372
        </li>
        <li>
          <svg viewBox="0 0 24 24" aria-hidden="true"><rect x="2" y="5" width="20" height="14" fill="#ee7325"/><path d="M2 5l10 8 10-8" fill="none" stroke="#fff" stroke-width="2"/></svg>
          hello@mailbox.com
        </li>
        <li>
          <svg viewBox="0 0 24 24" aria-hidden="true"><g fill="none" stroke="#ee7325" stroke-width="2"><circle cx="12" cy="12" r="10"/><ellipse cx="12" cy="12" rx="4" ry="10"/><path d="M2 12h20M4 7h16M4 17h16"/></g></svg>
          <span>www.<span class="accent">sitename</span>.com</span>
        </li>
      </ul>
      <p class="address">421, Address line goes here<br>45452, Country Name</p>
    </div>
  </section>

</body>
</html>
```